Biz technology consulting firm like a global company (better than Corvantis, etc)

Check word document high level requirements, a_design_webpage_content attached providing more details for content and message to convey to potential customers..  Create a crisp, clear and engaging business consulting website design that allows the user to understand the value that Brimquarta can deliver to their company.  We focus on innovation, simplification, creative solutions, digital transformations ERP, CRM, Analytics, project management, making IT simple and coaching enterprises how to align and implement technologies to support business strategy and goals. Whether a startup or a global billion dollar firm, we increase EBITDA through innovation and digital transformation.  

I desire to have sections that highlight each of the core areas such as: (**Please see  brimquarta.example and the design word document that is attached below for core areas of focus**)

Feel free to go to Brimquarta.example and review the basic categories to understand at a very high level the categories that are key.

Help me create a brand and website that engages startups, Private Equity firms seeking carve-out, integration experience and large corporate enterprises searching to convert to data driven and customer focused enterprises.  
Hero section with a tagline that emphasizes the company's focus on Walking UP bolder.  We help you visualize outcomes with a positive and collaborative solution driven mindset.  When you look at life through a different "positive" lens, you can convert all problems to opportunities.  Align your IT team with your business goals and you quickly realize the value of all processes and technology deployed in your enterprise; increasing EBITDA, morale, and long term success.

We evaluate your current state, create a custom roadmap for alignment, coach  and empower you to lead while removing the uncertainty and silos.  Partner with the experts who help make business and technology simple and effective
Call-to-action section encouraging visitors to learn more about the company's services and expertise
Services -- detail provided in the attached word document (please use)
Section providing an overview of the company's services, including digital transformation, strategy, change management, CRM, ERP, automation, AI, data / analytics, process optimization, carve-outs, integrations, scaling, risk mitigation, security and marketing.
Call-to-action section encouraging visitors to learn more about the company's expertise and how it can help their business and encouraging visitors to schedule a consultation or assessment.
Footer
Navigation menu
Contact information
LinkedIn link
The website should have a modern and professional design, with a focus on clear messaging and easy navigation. The color scheme will be clean and simple, with a mix of colors to convey trust, reliability, and innovation. The website will be optimized for search engines and mobile devices, ensuring that visitors can easily access the site from any device.

Target Market(s)

Companies who desire to grow their business, optimize their processes, maximize the output of human capital and profitablity.

Industry/Entity Type

Business Technology consulting

Coding

Coded - Design and coding required

Number of Pages Required

4 page

Font styles to use
Other font styles liked:
• designer should choose for professional audience

Requirements
Must have
• easy navigation, engaging flow, professional layout and colors that represent confidence, excellence and innovation in a world full of change.
Nice to have
• I would like to see you blend in the play on DELTA's (changes that we face in business and life), the different way we may look at things and the unique way we solve problems. All of these are options to Walk UP bolder and leverage the unique views of individuals, millions of data points, workflow and technology enablers to deliver maximize value to your enterprise

```html
<!DOCTYPE html>
<html lang="en">
<head>
<meta charset="utf-8">
<title>Brimquarta — Walk UP Bolder</title>
<link rel="stylesheet" href="https://fonts.googleapis.com/css2?family=Zilla+Slab:wght@500;600;700&family=Mulish:wght@400;600;700&display=swap">
<style>
:root{
  --pink:#f5085f;
  --cyan:#0aaedc;
  --orange:#f8a11c;
  --ink:#111111;
  --text:#333333;
  --muted:#f4f4f4;
  --white:#ffffff;
  --line:#dcdcdc;
}
*{margin:0;padding:0;box-sizing:border-box}
html,body{width:1200px;height:3829px;overflow:hidden}
body{position:relative;background:var(--white);font-family:"Mulish",Arial,sans-serif;color:var(--text)}
.slab{font-family:"Zilla Slab",Georgia,serif}
.abs{position:absolute}
.btn{position:absolute;display:flex;align-items:center;justify-content:center;font-family:"Zilla Slab",Georgia,serif;font-weight:700;color:var(--white);font-size:17px;border-radius:8px 22px 8px 22px}
.btn--orange{background:var(--orange)}
.btn--pink{background:var(--pink)}
.btn--cyan{background:var(--cyan)}

/* hero */
.hero{position:absolute;left:0;top:0;width:1200px;height:702px;background:linear-gradient(120deg,#e9e9e9 0%,#d6d6d6 45%,#bdbdbd 70%,#cfcfcf 100%)}
.hero__photo{position:absolute;inset:0;background:radial-gradient(ellipse 260px 340px at 640px 330px,rgba(90,90,90,.35),transparent 70%),radial-gradient(ellipse 380px 140px at 420px 580px,rgba(255,255,255,.5),transparent 70%)}
.logo{position:absolute;left:108px;top:18px;font-family:"Zilla Slab",Georgia,serif;font-weight:600;font-size:28px;color:var(--ink);letter-spacing:.5px}
.nav{position:absolute;top:27px;left:688px;display:flex;gap:30px;font-family:"Zilla Slab",Georgia,serif;font-weight:600;font-size:14px;color:var(--ink)}
.hero__kicker{position:absolute;top:282px;left:0;width:1200px;text-align:center;font-family:"Zilla Slab",Georgia,serif;font-weight:500;font-size:33px;color:var(--cyan)}
.hero__title{position:absolute;top:320px;left:0;width:1200px;text-align:center;font-family:"Zilla Slab",Georgia,serif;font-weight:700;font-size:76px;color:var(--ink);letter-spacing:1px}
.dot{position:absolute;border-radius:50%}

/* intro */
.intro__visual{position:absolute;left:129px;top:786px;width:408px;height:408px;border-radius:50%;background:radial-gradient(circle at 45% 40%,#e36bd8 0%,#4a5fd6 30%,#1a2d6e 60%,#0c1230 100%)}
.intro__title{position:absolute;left:575px;top:846px;width:520px;font-family:"Zilla Slab",Georgia,serif;font-weight:600;font-size:33px;line-height:46px;color:var(--ink)}
.intro__text{position:absolute;left:575px;top:960px;width:480px;font-size:14.5px;line-height:30px;color:var(--text)}

/* services */
.services{position:absolute;left:0;top:1300px;width:1200px;height:695px;background:var(--muted)}
.section-title{position:absolute;left:0;width:1200px;text-align:center;font-family:"Zilla Slab",Georgia,serif;font-weight:600;font-size:33px;color:var(--ink)}
.card{position:absolute;background:var(--white);border-radius:14px;box-shadow:0 4px 18px rgba(0,0,0,.04)}
.card__img{position:absolute;border-radius:4px}
.card__name{position:absolute;left:0;width:100%;text-align:center;font-family:"Zilla Slab",Georgia,serif;font-weight:600;font-size:18px;line-height:26px;color:var(--ink)}
.learn{position:absolute;display:flex;align-items:center;justify-content:center;background:var(--cyan);color:var(--white);font-family:"Mulish",Arial,sans-serif;font-weight:700;font-size:11px;border-radius:6px 16px 6px 16px}
.arrow{position:absolute;width:26px;height:26px;border-radius:50%;display:flex;align-items:center;justify-content:center}

/* innovative */
.innov{position:absolute;left:0;top:1995px;width:1200px;height:374px;background:linear-gradient(100deg,#f20a63 0%,#f4085c 60%,#ee1766 100%)}
.innov__title{position:absolute;top:72px;left:0;width:1200px;text-align:center;font-family:"Zilla Slab",Georgia,serif;font-weight:600;font-size:33px;color:var(--white)}
.innov__text{position:absolute;top:127px;left:160px;width:880px;text-align:center;font-size:15px;line-height:30px;color:var(--white)}

/* expertise */
.step__badge{position:absolute;width:66px;height:66px;border-radius:50%;border:3px solid #fff;box-shadow:0 0 0 1px rgba(0,0,0,.04);color:var(--white);text-align:center;font-family:"Zilla Slab",Georgia,serif}
.step__num{display:block;font-weight:700;font-size:27px;line-height:26px;margin-top:9px}
.step__lbl{display:block;font-size:11px;font-weight:600}
.step__card{position:absolute;top:2568px;height:231px;background:var(--white);border-radius:12px;box-shadow:0 4px 22px rgba(0,0,0,.07);padding:30px 28px;font-size:13px;line-height:26px;color:var(--text)}

/* vision */
.vision{position:absolute;left:149px;top:2953px;width:925px;height:323px;border-radius:10px;background:linear-gradient(180deg,#f8a31b 0%,#f59d12 100%)}
.vision__title{position:absolute;top:84px;left:0;width:100%;text-align:center;font-family:"Zilla Slab",Georgia,serif;font-weight:600;font-size:33px;color:var(--ink)}
.vision__text{position:absolute;top:130px;left:115px;width:695px;text-align:center;font-size:14.5px;line-height:26px;color:#2a2a2a}

/* footer */
.footer__brand{position:absolute;top:3336px;left:0;width:1200px;text-align:center;font-family:"Zilla Slab",Georgia,serif;font-weight:600;font-size:62px;color:var(--ink)}
.rule{position:absolute;left:119px;width:962px;height:1px;background:var(--line)}
.fcol{position:absolute;top:3502px}
.fcol h4{font-family:"Zilla Slab",Georgia,serif;font-weight:600;font-size:20px;color:var(--ink);margin-bottom:14px}
.fcol li{list-style:none;font-size:15px;line-height:30px;color:var(--text);display:flex;align-items:center;gap:6px}
.copy{position:absolute;top:3754px;left:0;width:1200px;text-align:center;font-size:14.5px;color:var(--text)}
.copy a{color:var(--cyan);text-decoration:underline}
</style>
</head>
<body>

<!-- Hero -->
<header class="hero">
  <div class="hero__photo" role="img" aria-label="Greyscale photo of a professional working at a desk in a modern office"></div>
  <div class="logo">BRIMQUARTA</div>
  <nav class="nav"><span>Home</span><span>About Us</span><span>Our Services</span><span>Blog</span><span>Contact</span></nav>
  <span class="dot" style="left:106px;top:112px;width:32px;height:32px;background:var(--cyan)"></span>
  <span class="dot" style="left:453px;top:122px;width:30px;height:30px;background:var(--cyan)"></span>
  <span class="dot" style="left:303px;top:180px;width:30px;height:30px;background:var(--orange)"></span>
  <span class="dot" style="left:766px;top:132px;width:22px;height:22px;background:var(--pink)"></span>
  <span class="dot" style="left:1069px;top:162px;width:30px;height:30px;background:var(--orange)"></span>
  <span class="dot" style="left:575px;top:230px;width:34px;height:34px;background:var(--orange)"></span>
  <span class="dot" style="left:385px;top:464px;width:30px;height:30px;background:var(--orange)"></span>
  <span class="dot" style="left:599px;top:468px;width:20px;height:20px;background:var(--pink)"></span>
  <span class="dot" style="left:113px;top:550px;width:28px;height:28px;background:var(--pink)"></span>
  <span class="dot" style="left:1133px;top:569px;width:40px;height:40px;background:var(--pink)"></span>
  <span class="dot" style="left:284px;top:609px;width:32px;height:32px;background:var(--cyan)"></span>
  <span class="dot" style="left:727px;top:613px;width:32px;height:32px;background:var(--orange)"></span>
  <div class="hero__kicker">WELCOME TO BRIMQUARTA</div>
  <h1 class="hero__title">WALK UP BOLDER</h1>
  <a class="btn btn--orange" style="left:514px;top:421px;width:156px;height:50px">Get Started</a>
</header>

<!-- Intro -->
<section class="intro">
  <div class="intro__visual" role="img" aria-label="Illustration of a glowing digital city with data dashboards"></div>
  <h2 class="intro__title">TRANSFORMING THE WAY YOU DO BUSINESS</h2>
  <p class="intro__text">Every business is unique. That's why we take a personalized approach to every project, working closely with you to understand your goals and create tailored solutions that work for you.</p>
  <a class="btn btn--pink" style="left:578px;top:1068px;width:156px;height:50px">Get Started</a>
</section>

<!-- Services -->
<section class="services">
  <h2 class="section-title" style="top:90px">OUR SERVICES</h2>
  <div class="arrow" style="left:24px;top:354px;background:var(--pink)"><svg width="10" height="10" viewBox="0 0 10 10"><path d="M6.5 2 3.5 5l3 3" fill="none" stroke="#fff" stroke-width="1.6"/></svg></div>
  <div class="arrow" style="left:1139px;top:354px;background:#fff;box-shadow:0 1px 4px rgba(0,0,0,.15)"><svg width="10" height="10" viewBox="0 0 10 10"><path d="M3.5 2 6.5 5l-3 3" fill="none" stroke="#333" stroke-width="1.4"/></svg></div>

  <div class="card" style="left:67px;top:264px;width:236px;height:256px">
    <div class="card__img" style="left:15px;top:-70px;width:206px;height:225px;background:linear-gradient(160deg,#8fa0a8,#5c6a70 60%,#3b4448)" role="img" aria-label="Photo of a team planning on a whiteboard covered in sticky notes"></div>
    <div class="card__name" style="top:184px">DIGITAL<br>TRANSFORMATION</div>
  </div>
  <div class="card" style="left:327px;top:264px;width:278px;height:329px">
    <div class="card__img" style="left:20px;top:-84px;width:242px;height:265px;background:linear-gradient(160deg,#e6e6e6,#b9b7b2 55%,#6e6358)" role="img" aria-label="Photo of a consultant presenting strategy to colleagues"></div>
    <div class="card__name" style="top:218px">STRATEGY</div>
    <div class="learn" style="left:74px;top:260px;width:128px;height:34px">LEARN MORE</div>
  </div>
  <div class="card" style="left:630px;top:264px;width:237px;height:256px">
    <div class="card__img" style="left:15px;top:-70px;width:206px;height:225px;background:linear-gradient(160deg,#0b2a6a,#1d5fc4 55%,#0a1e45)" role="img" aria-label="Illustration of a laptop with change management graphics"></div>
    <div class="card__name" style="top:184px">CHANGE<br>MANAGEMENT</div>
  </div>
  <div class="card" style="left:889px;top:264px;width:237px;height:256px">
    <div class="card__img" style="left:15px;top:-70px;width:206px;height:225px;background:linear-gradient(160deg,#c8d6e4,#7d93a8 55%,#3e4d5c)" role="img" aria-label="Photo of hands holding a tablet in an automated factory"></div>
    <div class="card__name" style="top:196px">AUTOMATION</div>
  </div>
</section>

<!-- Innovative solutions -->
<section class="innov" role="region" aria-label="Innovative solutions">
  <h2 class="innov__title">INNOVATIVE SOLUTIONS</h2>
  <p class="innov__text">We believe in pushing the boundaries of what is possible. Our team of experts are dedicated to crafting innovative solutions that help your business thrive. From cutting-edge AI and analytics to customer loyalty and digital transformation, we provide what you need to succeed in today's fast-paced business world.</p>
  <a class="btn btn--cyan" style="left:527px;top:242px;width:156px;height:50px">Get Started</a>
</section>

<!-- Expertise -->
<section class="expertise">
  <h2 class="section-title" style="top:2430px">OUR COMPANY EXPERTISE</h2>
  <svg class="abs" style="left:0;top:2548px" width="1200" height="2"><line x1="150" y1="1" x2="1200" y2="1" stroke="#cfcfcf" stroke-dasharray="3 3"/></svg>

  <div class="step__card" style="left:159px;width:263px">Initial Conversations and Process Discovery: Engaging in initial conversations with key IT and operations leaders to understand the current state of processes and identify areas for improvement that align with business goals.</div>
  <div class="step__card" style="left:470px;width:260px">Review of Documentation: Assessing the level of completeness, accuracy, and date stamp of IT documentation to ensure that improvements are aligned with business objectives and promote business continuity.</div>
  <div class="step__card" style="left:776px;width:263px">IT Roadmap Visibility and Awareness: Improving IT roadmap visibility and awareness throughout the organization to ensure that identified areas for improvement are aligned with critical business initiatives and strategic objectives.</div>
  <div class="step__card" style="left:1080px;width:263px;opacity:.55">IT Roadmap Visibility and Awareness: Improving IT roadmap visibility and awareness throughout the organization to ensure that identified areas for improvement are aligned with critical business initiatives and strategic objectives.</div>

  <div class="step__badge" style="left:185px;top:2514px;background:var(--pink)"><span class="step__num">01</span><span class="step__lbl">Step</span></div>
  <div class="step__badge" style="left:494px;top:2514px;background:var(--orange)"><span class="step__num">02</span><span class="step__lbl">Step</span></div>
  <div class="step__badge" style="left:802px;top:2514px;background:var(--cyan)"><span class="step__num">03</span><span class="step__lbl">Step</span></div>
  <div class="step__badge" style="left:1105px;top:2514px;background:#f57aa6"><span class="step__num">04</span><span class="step__lbl">Step</span></div>

  <div class="arrow" style="left:61px;top:2659px;background:var(--pink)"><svg width="10" height="10" viewBox="0 0 10 10"><path d="M6.5 2 3.5 5l3 3" fill="none" stroke="#fff" stroke-width="1.6"/></svg></div>
  <div class="arrow" style="left:1136px;top:2659px;background:#eee"><svg width="10" height="10" viewBox="0 0 10 10"><path d="M3.5 2 6.5 5l-3 3" fill="none" stroke="#333" stroke-width="1.4"/></svg></div>

  <a class="btn btn--orange" style="left:461px;top:2833px;width:277px;height:49px">Schedule A Consultation</a>
</section>

<!-- Vision -->
<section class="vision" role="region" aria-label="Unlock potential of vision">
  <h2 class="vision__title">UNLOCK POTENTIAL OF VISION</h2>
  <p class="vision__text">Our team of experts consists of professionals with extensive transformation experience spanning a variety of industries.&nbsp; We are committed to help our clients achieve their goals.</p>
  <a class="btn btn--cyan" style="left:372px;top:200px;width:156px;height:50px">Get Started</a>
</section>

<!-- Footer -->
<footer>
  <div class="footer__brand">BRIMQUARTA</div>
  <div class="rule" style="top:3457px"></div>
  <div class="fcol" style="left:129px"><h4>QUICK LINKS</h4><ul><li>Home</li><li>About Us</li><li>Our Services</li><li>Blog</li><li>Contact</li></ul></div>
  <div class="fcol" style="left:357px"><h4>CUSTOMER CARE</h4><ul>
    <li><svg width="12" height="14" viewBox="0 0 12 14"><path d="M6 13S1.5 8 1.5 5a4.5 4.5 0 0 1 9 0C10.5 8 6 13 6 13z" fill="var(--pink)"/><circle cx="6" cy="5" r="1.6" fill="#fff"/></svg>12b Brimquarta Lorem ipsum dolor</li>
    <li><svg width="13" height="13" viewBox="0 0 14 14"><path d="M3 1l2.5 3-1.5 1.5a8 8 0 0 0 4.5 4.5L10 8.5l3 2.5-1.5 2.5C6 13 1 8 .5 2.5z" fill="var(--pink)"/></svg>+1 555 014 2290</li>
    <li><svg width="14" height="11" viewBox="0 0 14 11"><rect x=".7" y=".7" width="12.6" height="9.6" rx="1" fill="none" stroke="var(--pink)" stroke-width="1.3"/><path d="M1 1l6 5 6-5" fill="none" stroke="var(--pink)" stroke-width="1.3"/></svg>info@brimquarta.example</li>
  </ul></div>
  <div class="fcol" style="left:694px"><h4>OTHER LINKS</h4><ul><li>Terms &amp; conditions</li><li>Privacy Policy</li><li>About Us</li><li>Support</li></ul></div>
  <div class="fcol" style="left:919px"><h4>FOLLOW US</h4><ul><li><span style="display:inline-block;width:28px;height:28px;border-radius:50%;background:var(--cyan)" aria-label="Professional network link"></span></li></ul></div>
  <div class="rule" style="top:3725px"></div>
  <p class="copy">©Copyrights 2023 &nbsp;<a>Brimquarta.</a> &nbsp; | &nbsp;&nbsp; All Rights Reserved</p>
</footer>

</body>
</html>
```